International MultiIndustry Team Coaching Site

Hello Designers,
We need a redesign of the pages attached.
The design must be engaging and modern, with a focus on the user experience, particularly for the "observations" page. Because this is the main page of the website. It is to be used on a 10'' tablet or desktop, to record observations on the fly, so it must be intuitive and efficient.
The positioning of the metrics and observations and etc, are just a reference. you can switch it up if you feel there is a better way (PLEASE DO ;) ).

There are many categories (color coded with borders in the example hpt_6_observations.jpg) and observation metrics within each category. This is the Key page, because it is the One with the most interactions.

The user should know when it has selected a category (there should be some visual hint) and the different metric widgets should be accounted for.
There are 3: The time widget at the end, numerical widgets (recording more or less numbers), and boolean ones (selected or not).

For the numerical widgets, we show plus and minus characters, but you can change this, being creative, keeping in mind that it must work well on a mobile device and desktop, and must be intuitive and quick.

Set your creativity free with the login screen , home screen, categories secret, events screen, journaling and observations screen .

We would like the site/mobile version to have a very modern look. Something that would be found in very popular and user friendly apps.

***** The events, journaling, category and home screens are getting 2 much attention , please focus also on the observations screen *******
Imagine you are a psychologist tasked with observing the behaviour of teenagers during group work. And you have a tablet on which to record what you observe. Now imagine you need to observe during 3 classes: Biology, Math, Physics (these are events). For each class (event) you will have to record observations in 3 categories: Social Interaction, Leadership, Communication (these are categories).
Example of the metrics (these are observations) for Leadership:
" the teenager direct other colleagues" (boolean widget),
"the teenager speaks more than everyone else" (boolean widget)
"the teenager interrupts colleagues speaking" (number widget)
"the work took hh:mm" (time widget)

The observations screen can have any shape and form you think of. It doesn't need to be that single column with yes and nos, or that double column with the squared cards.
thank you.

Hope that was useful intel :)
Available for any questions you might have.
Good luck :)

Enterprise teams

5+ page

Sans Serif

• Modern design

```html
<!DOCTYPE html>
<html lang="en">
<head>
<meta charset="utf-8">
<title>Mentora — Sign In</title>
<link rel="stylesheet" href="https://fonts.googleapis.com/css2?family=Poppins:wght@400;500;600;700&display=swap">
<style>
  :root {
    --page-bg: #f6f8fc;
    --wave-blue: #e3ebf8;
    --wave-violet: #ebe8f7;
    --card-bg: #ffffff;
    --ink: #0c0c14;
    --title: #252d55;
    --accent-blue: #4f86c6;
    --field-border: #dcdfe6;
    --placeholder: #8b90a3;
    --icon: #9a9fb0;
    --link: #4a7fc1;
    --primary: #c04d74;
    --on-primary: #ffffff;
  }
  * { box-sizing: border-box; margin: 0; padding: 0; }
  html, body {
    width: 1200px;
    height: 696px;
    overflow: hidden;
    font-family: "Poppins", sans-serif;
    background: var(--page-bg);
  }
  .stage {
    position: relative;
    width: 1200px;
    height: 696px;
    overflow: hidden;
  }
  .backdrop {
    position: absolute;
    inset: 0;
    background:
      radial-gradient(ellipse 420px 160px at 180px 380px, var(--wave-blue), transparent 70%),
      radial-gradient(ellipse 380px 140px at 1050px 420px, var(--wave-violet), transparent 70%),
      radial-gradient(ellipse 300px 120px at 1100px 540px, var(--wave-blue), transparent 70%),
      radial-gradient(circle 200px at 130px 180px, #eef2fa, transparent 70%),
      linear-gradient(180deg, #f8f9fc 0%, #f3f6fb 55%, #f7f8fc 100%);
  }
  .brand {
    position: absolute;
    left: 0;
    right: 0;
    top: 121px;
    display: flex;
    justify-content: center;
    align-items: center;
    gap: 12px;
  }
  .brand-mark {
    width: 30px;
    height: 30px;
    border-radius: 5px;
    background: var(--accent-blue);
  }
  .brand-name {
    font-size: 35px;
    font-weight: 700;
    color: var(--ink);
    line-height: 1;
  }
  .signin-card {
    position: absolute;
    left: 404px;
    top: 219px;
    width: 392px;
    height: 321px;
    background: var(--card-bg);
    border-radius: 7px;
    box-shadow: 0 4px 24px rgba(60, 80, 130, 0.06);
  }
  .card-title {
    position: absolute;
    left: 31px;
    top: 22px;
    font-size: 22px;
    font-weight: 600;
    color: var(--title);
    line-height: 1.4;
  }
  .card-title::after {
    content: "";
    position: absolute;
    left: 0;
    top: 36px;
    width: 50px;
    height: 2px;
    background: var(--accent-blue);
  }
  .field {
    position: absolute;
    left: 29px;
    width: 334px;
    height: 43px;
    border: 1px solid var(--field-border);
    border-radius: 4px;
    display: flex;
    align-items: center;
    padding-left: 15px;
    gap: 12px;
  }
  .field-email { top: 84px; }
  .field-password { top: 145px; }
  .field svg { flex: none; }
  .field-placeholder {
    font-size: 12.5px;
    color: var(--placeholder);
  }
  .forgot-link {
    position: absolute;
    right: 29px;
    top: 205px;
    font-size: 12.5px;
    color: var(--link);
    text-decoration: none;
  }
  .signin-button {
    position: absolute;
    left: 128px;
    top: 249px;
    width: 135px;
    height: 43px;
    border: none;
    border-radius: 6px;
    background: var(--primary);
    color: var(--on-primary);
    font-family: "Poppins", sans-serif;
    font-size: 15px;
    font-weight: 600;
  }
</style>
</head>
<body>
  <main class="stage">
    <div class="backdrop" role="img" aria-label="Soft abstract background of flowing pale blue and violet light waves with blurred dots"></div>

    <header class="brand">
      <span class="brand-mark"></span>
      <span class="brand-name">Mentora</span>
    </header>

    <section class="signin-card">
      <h1 class="card-title">Sign In</h1>

      <div class="field field-email">
        <svg width="22" height="16" viewBox="0 0 22 16" fill="none" stroke="var(--icon)" stroke-width="1.2">
          <rect x="0.6" y="0.6" width="20.8" height="14.8" rx="1"/>
          <path d="M0.8 1 L11 9 L21.2 1"/>
        </svg>
        <span class="field-placeholder">Enter your email</span>
      </div>

      <div class="field field-password">
        <svg width="22" height="22" viewBox="0 0 22 22" fill="none" stroke="var(--icon)" stroke-width="1.2">
          <rect x="2" y="9" width="18" height="12" rx="1"/>
          <path d="M6 9 V6 a5 5 0 0 1 10 0 V9"/>
          <circle cx="11" cy="14" r="1.6"/>
          <path d="M11 15.6 V18"/>
        </svg>
        <span class="field-placeholder">Enter your password</span>
      </div>

      <a class="forgot-link" href="#">Forgot your password?</a>

      <button class="signin-button" type="button">Sign In</button>
    </section>
  </main>
</body>
</html>
```